Orthopedic Arm Surgeon Brochure

Bifold modern design. I will supply the text, my photo, and photos of my textbooks. Prefer colors in the greens, blues, greys. For more information visit LimbForwardClinic.com Please feel free to e-mail me with any questions. Current brochure attached; I want to modernize this, get rid of frames, and change the text.

Target Market(s)

High-end market

Colors
3176b5
33a6d7
33b8a4
abd036
876aae
b768aa

Requirements
Must have
• Beautiful finishes
Should not have
• Bright reds, yellows, oranges that emit fear

```html
<!DOCTYPE html>
<html lang="en">
<head>
<meta charset="utf-8">
<title>Crestline Orthopedic Group – Bifold Brochure</title>
<link href="https://fonts.googleapis.com/css2?family=PT+Serif:wght@400;700&family=Fira+Sans:wght@800&display=swap" rel="stylesheet">
<style>
:root{
  --lime:#a9cc2e;
  --lime-light:#d4e86a;
  --forest:#0b6a35;
  --green-text:#1d6b3a;
  --ink:#333;
  --paper:#fff;
  --stage:#000;
}
*{box-sizing:border-box;margin:0;padding:0}
html,body{width:1200px;height:961px;overflow:hidden;background:var(--stage)}
body{position:relative;font-family:"PT Serif",serif;color:var(--ink)}
.panel-label{position:absolute;color:#fff;font-size:21px;font-family:"PT Serif",serif}
.panel{position:absolute;width:494px;height:348px;background:var(--paper);overflow:hidden}
.wash{position:absolute;top:0;bottom:0}
.wash-right{right:0;width:240px;background:radial-gradient(ellipse at 70% 40%,#cfe24a 0%,#dcea86 45%,rgba(240,246,200,.6) 75%,rgba(255,255,255,0) 100%)}
.wash-left{left:0;width:250px;background:radial-gradient(ellipse at 20% 60%,#c8df3e 0%,#dbea82 45%,rgba(240,246,200,.6) 75%,rgba(255,255,255,0) 100%)}
.top-strip{position:absolute;top:0;left:0;right:0;height:10px;background:var(--forest)}
.top-pill{position:absolute;top:0;left:0;width:362px;height:17px;background:var(--lime);border-bottom-right-radius:12px}
.foot-lime{position:absolute;left:0;bottom:0;width:322px;height:38px;background:var(--lime);border-top-right-radius:20px}
.foot-forest{position:absolute;right:0;bottom:0;width:297px;height:26px;background:var(--forest);border-top-left-radius:18px;color:#fff;font-size:11.5px;display:flex;align-items:center;padding-left:20px}
.phone{position:absolute;left:22px;bottom:4px;font-family:"Fira Sans",sans-serif;font-weight:800;font-size:18px;color:#1b2a12;display:flex;align-items:center;gap:3px}
.phone svg{width:11px;height:11px}
.web{position:absolute;left:22px;top:286px;font-size:14.5px;color:#2b2b2b}
.photo{position:absolute;background:linear-gradient(135deg,#e6e6e6,#9a9a9a)}
.strip{position:absolute;left:21px;top:36px;width:451px;height:42px;border-top:1px solid var(--forest);border-bottom:1px solid var(--forest);display:flex;gap:2px;padding:2px 0}
.strip span{flex:1;background:linear-gradient(135deg,#f1f1f1 0%,#c9c9c9 55%,#e7b3b0 80%,#dcdcdc 100%)}
.heading{position:absolute;color:var(--green-text);font-size:13px;text-align:center;line-height:1;text-transform:uppercase}
.heading.mixed{text-transform:none}
.body-copy{position:absolute;font-size:5.6px;line-height:1.45;text-align:center;color:#333}
.body-copy p+p{margin-top:3px}
/* front */
.brand{position:absolute;left:30px;top:40px;display:flex;align-items:center;gap:8px}
.brand-dot{width:16px;height:16px;border-radius:50%;background:var(--forest)}
.brand-name{color:var(--forest);font-weight:700;font-size:25px;line-height:1}
.brand-sub{color:var(--forest);font-size:13px;margin-top:3px;font-weight:400}
.divider{position:absolute;left:262px;top:44px;width:1px;height:44px;background:var(--forest)}
.doctor{position:absolute;left:286px;top:46px}
.doctor h1{font-size:12px;color:var(--forest);font-weight:700}
.doctor p{font-size:5.8px;line-height:1.6;margin-top:2px}
.conditions{position:absolute;left:0;top:232px;width:494px;height:38px;display:flex}
.conditions li{list-style:none;color:var(--green-text);font-size:8.8px;padding:20px 4px 0;border-left:1px solid var(--forest)}
.conditions li:first-child{border-left:none;padding-left:24px}
/* back */
.portrait{position:absolute;left:44px;top:40px;width:106px;height:182px;background:linear-gradient(160deg,#d8d8d8,#5e5e5e)}
.bio{position:absolute;left:150px;top:50px;width:95px;border-left:1px solid #777;padding-left:10px;font-size:5.6px;line-height:1.5}
.bio p+p{margin-top:4px}
.book{position:absolute;width:42px;height:54px;box-shadow:1px 2px 3px rgba(0,0,0,.4);border:1px solid #fff}
.locations-band{position:absolute;left:0;top:264px;width:346px;height:32px;background:var(--lime);border-top-right-radius:18px;color:#2a3a10;font-size:9.2px;padding:10px 0 0 30px}
.locations{position:absolute;left:0;bottom:0;width:476px;height:56px;background:var(--forest);border-top-right-radius:24px;color:#fff;display:flex;padding:14px 0 0 30px}
.loc{font-size:8px;line-height:1.35;padding-right:6px}
.loc+.loc{border-left:1px solid #fff;padding-left:6px}
.loc b{font-weight:700}
</style>
</head>
<body>

<div class="panel-label" style="left:89px;top:99px">Front</div>
<div class="panel-label" style="left:615px;top:99px">Front Inside</div>
<div class="panel-label" style="left:89px;top:485px">Back</div>
<div class="panel-label" style="left:615px;top:485px">Back Inside</div>

<!-- Front cover -->
<section class="panel" style="left:90px;top:122px">
  <div class="top-strip"></div><div class="top-pill"></div>
  <div class="brand">
    <div class="brand-dot"></div>
    <div><div class="brand-name">CRESTLINE</div><div class="brand-sub">Orthopedic Group, L.L.P.</div></div>
  </div>
  <div class="divider"></div>
  <div class="doctor">
    <h1>Martin R. Halvorsen, MD</h1>
    <p>Specialist in Surgery of the Hand, Wrist, Elbow &amp; Shoulder<br>Board Certified Orthopedic Surgeon<br>Certificate of Additional Qualification, Hand Surgery</p>
  </div>
  <div class="photo" role="img" aria-label="Black and white photo of a man exercising with dumbbells" style="left:0;top:114px;width:126px;height:116px"></div>
  <div class="photo" role="img" aria-label="Black and white photo of a tennis player holding a racket" style="left:130px;top:114px;width:188px;height:116px"></div>
  <div class="photo" role="img" aria-label="Black and white photo of a person holding a sore wrist at a laptop" style="left:322px;top:114px;width:172px;height:116px"></div>
  <ul class="conditions">
    <li>CARPAL TUNNEL</li><li>CUBITAL TUNNEL</li><li>TRIGGER INGER</li><li>DEQUERVAIN'S TENDINITIS</li><li>ELBOW &amp; SHOULDER PAIN</li>
  </ul>
  <div class="web">www.LimbForwardClinic.com</div>
  <div class="foot-lime"></div>
  <div class="phone"><svg viewBox="0 0 12 12"><circle cx="6" cy="6" r="5" fill="none" stroke="#1b2a12" stroke-width="1.4"/><path d="M4 3.5c0 3 1.5 5 4 5" fill="none" stroke="#1b2a12" stroke-width="1.6"/></svg>7133-555-LIMB</div>
  <div class="foot-forest">Appointments can be made online through BookCareNow.com</div>
</section>

<!-- Front inside -->
<section class="panel" style="left:616px;top:122px">
  <div class="wash wash-right" role="img" aria-label="Lime watercolor wash"></div>
  <div class="top-strip"></div><div class="top-pill"></div>
  <div class="strip" role="img" aria-label="Row of photos showing painful hands, elbows and shoulders"><span></span><span></span><span></span><span></span><span></span><span></span><span></span><span></span></div>
  <h2 class="heading" style="left:72px;top:94px;width:160px">Carpal Tunnel<br>Syndrome</h2>
  <div class="body-copy" style="left:52px;top:120px;width:204px">
    <p>Carpal Tunnel Syndrome occurs when the median nerve to the hand gets pinched at the wrist. This leads to fingers feeling "numb", "asleep", "cold", like they "lack circulation" or have "pins and needles" in them. Carpal tunnel syndrome is usually worst at night or upon awakening. If you wake up at night with your hand numb or painfully asleep, and have to "shake it out" to get relief, you've probably got carpal tunnel syndrome. Symptoms also often occur with gripping, such as when driving, writing or holding books, cell phones or tools.</p>
    <p>Unless the carpal tunnel syndrome has led to nerve damage, initial treatment often involves splinting the wrist at night when asleep. If that doesn't work, the carpal tunnel can be released. The least invasive technique is the Single-Incision Endoscopic Carpal Tunnel Release. This quick, minimally invasive, outpatient procedure uses a small incision at the wrist without any incision in the hand. Compared to other techniques, there is decreased pain and a quicker return to work and other activities. There are no bandages, and hand washing and showering can be performed immediately. To see a video of an Endoscopic Carpal Tunnel Release please go to: www.LimbForwardClinic.com</p>
  </div>
  <h2 class="heading" style="left:284px;top:94px;width:160px">Cubital Tunnel<br>Syndrome</h2>
  <div class="body-copy" style="left:284px;top:120px;width:162px">
    <p>Cubital tunnel syndrome occurs when the funny bone (ulnar) nerve gets pinched at the elbow. This leads to tingling and numbness of the small finger when the elbow is bent, usually at night or when talking on the phone. Numbness may also occur when the elbow is placed on a hard surface.</p>
    <p>Unless nerve damage has occurred, treatment starts with avoiding pressure on the elbow, and not resting the elbow on desks, arm rests, or other hard objects. Avoid prolonged elbow flexion: use the other hand to hold phones or get a hands-free device.</p>
    <p>If this fails, the least invasive definitive treatment is an Endoscopic Cubital Tunnel Release. This minimally invasive, outpatient procedure allows an early return to activities with a low complication rate. No splint is used after surgery. To see a video of an Endoscopic Cubital Tunnel Release please go to: www.LimbForwardClinic.com</p>
  </div>
  <div class="web">www.LimbForwardClinic.com</div>
  <div class="foot-lime"></div>
  <div class="phone"><svg viewBox="0 0 12 12"><circle cx="6" cy="6" r="5" fill="none" stroke="#1b2a12" stroke-width="1.4"/><path d="M4 3.5c0 3 1.5 5 4 5" fill="none" stroke="#1b2a12" stroke-width="1.6"/></svg>7133-555-LIMB</div>
  <div class="foot-forest">Appointments can be made online through BookCareNow.com</div>
</section>

<!-- Back -->
<section class="panel" style="left:90px;top:509px">
  <div class="wash wash-right" role="img" aria-label="Lime watercolor wash" style="width:300px"></div>
  <div class="top-strip"></div><div class="top-pill"></div>
  <div class="portrait" role="img" aria-label="Black and white portrait of the doctor in a suit"></div>
  <div class="bio">
    <p><b>Dr. Halvorsen</b> is a nationally-recognized Upper Extremity Surgeon who has edited 7 textbooks, published over 45 original research papers and written 23 textbook chapters.</p>
    <p>Dr. Halvorsen graduated Cum Laude from Easton University and with honors from Northfield Medical School. He completed his residency in Orthopaedic Surgery at Westbrook University. In order to obtain expertise covering the entire upper extremity, he completed two fellowships, one in Hand Surgery and the other in Sports Medicine. He is board certified in Orthopaedic Surgery and has a Certificate of Additional Qualification in Hand Surgery.</p>
  </div>
  <div class="book" role="img" aria-label="Textbook cover" style="left:277px;top:78px;background:linear-gradient(160deg,#2a4a78,#b89a5a)"></div>
  <div class="book" role="img" aria-label="Textbook cover" style="left:326px;top:78px;background:linear-gradient(160deg,#3a2e6e,#6a4d8e)"></div>
  <div class="book" role="img" aria-label="Textbook cover" style="left:377px;top:78px;background:linear-gradient(160deg,#1f7fc4,#7fc0e6)"></div>
  <div class="book" role="img" aria-label="Textbook cover" style="left:430px;top:78px;background:linear-gradient(160deg,#6b4a2a,#3b5e7a)"></div>
  <div class="book" role="img" aria-label="Textbook cover" style="left:306px;top:147px;background:linear-gradient(160deg,#8a1e2a,#4a0e18)"></div>
  <div class="book" role="img" aria-label="Textbook cover" style="left:354px;top:147px;background:linear-gradient(160deg,#cfd8e4,#2c4a7a)"></div>
  <div class="book" role="img" aria-label="Textbook cover" style="left:402px;top:147px;background:linear-gradient(160deg,#5a2e6e,#c47a3a)"></div>
  <div class="locations-band">DR. HALVORSEN SEES PATIENTS AT THE FOLLOWING LOCATIONS:</div>
  <div class="locations">
    <div class="loc"><b>Bayou Medical Center</b><br>4200 Larkspur Street Suite 310<br>Houston, Texas 77030</div>
    <div class="loc"><b>Pearland</b><br>2215 Oak Meadow Dr<br>Suite 104 Pearland, Texas 77584</div>
    <div class="loc"><b>Katy</b><br>918 Willow Bend Dr.<br>Katy, Texas 77450</div>
    <div class="loc"><b>Cyfair</b><br>7350 Cedar Ridge Road<br>Houston, Texas 77065</div>
  </div>
</section>

<!-- Back inside -->
<section class="panel" style="left:616px;top:509px">
  <div class="wash wash-left" role="img" aria-label="Lime watercolor wash"></div>
  <div class="top-strip"></div><div class="top-pill"></div>
  <div class="strip" role="img" aria-label="Row of photos showing painful hands, elbows and shoulders"><span></span><span></span><span></span><span></span><span></span><span></span><span></span><span></span></div>
  <h2 class="heading" style="left:40px;top:93px;width:160px">Trigger Finger</h2>
  <div class="body-copy" style="left:52px;top:110px;width:144px">
    <p>Trigger finger occurs when the tendon that moves the finger gets pinched in its tunnel. This causes the finger to get stuck or stiff, which is often worse in the morning. This catching or locking can be quite painful. Grip may also cause pain. The finger may occasionally get stuck straight and be difficult to bend.</p>
    <p>Splinting may temporarily prevent the catching, but doesn't actually treat the problem. If caught early, a steroid injection can be curative. After 4-6 months the chance of an injection permanently curing the condition is lower, but still often worth a try.</p>
    <p>If the triggering returns following an injection, the problem can be definitively treated with a minimally-invasive Trigger Finger Release. This highly successful outpatient surgery is almost always a permanent cure. To see a video of a Trigger Finger Release please go to: www.LimbForwardClinic.com</p>
  </div>
  <h2 class="heading" style="left:248px;top:93px;width:160px">Wrist Pain</h2>
  <div class="body-copy" style="left:212px;top:110px;width:232px">
    <p>Wrist pain may have many causes and the diagnosis is best made by a fellowship-trained Hand Surgeon. The most common cause is DeQuervain's tendinitis, which causes pain on the thumb side of the wrist. This occurs when the tendons to the thumb and wrist get pinched in their tunnel. Pain is usually worse with lifting and gripping.</p>
    <p>DeQuervain's Tendinitis is common in mothers who repetitively lift children. It can also occur following frequent lifting with the thumb up, such as when pulling weeds or moving heavy objects.</p>
    <p>Initial treatment is to avoid lifting with the thumb up. If lifting is necessary, lift with the palm up or the palm down. To lift small children, keep the palm up and 'scoop under' the child. Use the other hand to bear most of the weight. A single steroid injection often helps by decreasing inflammation in the tunnel. In mild cases, this can be curative, especially if the problem is treated early and stressful activities can be avoided. Unfortunately, sometimes there's a very small second tunnel that causes problems and doesn't respond well to injections.</p>
    <p>If the tendinitis recurs after injection, an outpatient tendon release is very effective. To prevent tendon subluxation after tunnel release, I lengthen the restraints that stabilize the tendon and repair them in a lengthened position. To see a video of a DeQuervain's Tendinitis Release please go to: www.LimbForwardClinic.com</p>
  </div>
  <div class="web">www.LimbForwardClinic.com</div>
  <div class="foot-lime"></div>
  <div class="phone"><svg viewBox="0 0 12 12"><circle cx="6" cy="6" r="5" fill="none" stroke="#1b2a12" stroke-width="1.4"/><path d="M4 3.5c0 3 1.5 5 4 5" fill="none" stroke="#1b2a12" stroke-width="1.6"/></svg>7133-555-LIMB</div>
  <div class="foot-forest">Appointments can be made online through BookCareNow.com</div>
</section>

</body>
</html>
```